Business Card Design

We like to use greens as you will see in our logo (but not TOO much green). We are a Dental Clinic in a somewhat eccentric community. We do not like the dated sharp designs which we see many dentists use. We're looking for something bright and fresh while still maintaining the integrity of the profession. Elegance is not necessarily what we are going for... we need for the design to be "mature" but also up-lifting.

See our logo.
Updates

Project Deadline Extended
Reason: We have 5 designs which we like. But we'd like to see a few more before committing to a design.

Project Deadline Extended
Reason: We are awaiting revisions to this project. We are still welcoming designs while we wait to see if designers are able to provide to us the revisions we require in order to proceed with a selection.

Target Market(s)

Younger families - ages late 20's to early 40's

Industry/Entity Type

Business

Contact Information for Business Card

Marlow T. Benning DDS 2740 W. Hollister Rd. Ste. 7 Royal Oak, MI 48133 (248)555-0193 FX (248)555-0147 info@BrightwellDentalCareMi.example BrigthwellDentalCareMi.example on the back of the card we need an appointment reminder (For____ Date___ Time____) with "If you are unable to keep your appointment, kindly give 48 hours notice" at the bottom. No use of teeth in the design. DOUBLE SIDED DESIGN

Requirements
Should not have
• The use of pictures of teeth

```html
<!DOCTYPE html>
<html lang="en">
<head>
<meta charset="utf-8">
<title>Brightwell Dental Care – Business Card</title>
<link rel="stylesheet" href="https://fonts.googleapis.com/css2?family=Open+Sans:wght@300;400;600;700&display=swap">
<style>
  :root {
    --page: #eceee9;
    --card-white: #ffffff;
    --green-deep: #3f9a2c;
    --green-mid: #5cb338;
    --green-light: #8fcb5a;
    --green-pale: #c9e6ae;
    --green-ink: #2f7d2a;
    --text-grey: #4a4a4a;
  }
  * { box-sizing: border-box; margin: 0; padding: 0; }
  html, body {
    width: 1200px; height: 1024px; overflow: hidden;
    background: var(--page);
    font-family: "Open Sans", Arial, sans-serif;
  }
  .canvas { position: relative; width: 1200px; height: 1024px; }

  .card {
    position: absolute; left: 240px; width: 720px; height: 411px;
    overflow: hidden; border-radius: 4px;
    box-shadow: 0 6px 18px rgba(0,0,0,.18);
  }
  .card--front { top: 70px; background: var(--card-white); }
  .card--back {
    top: 543px;
    background: linear-gradient(135deg, var(--green-deep) 0%, var(--green-mid) 55%, var(--green-light) 100%);
    color: #fff;
  }

  /* front */
  .corner-square {
    position: absolute; right: 0; top: 0; width: 150px; height: 90px;
    background: linear-gradient(135deg, var(--green-light), var(--green-mid));
  }
  .brand {
    position: absolute; left: 300px; top: 30px; width: 250px;
    display: flex; align-items: center; gap: 14px;
  }
  .brand__dot { width: 34px; height: 34px; border-radius: 50%; background: var(--green-mid); flex: none; }
  .brand__name {
    font-weight: 300; font-size: 30px; line-height: 1.1; color: var(--green-ink);
  }
  .brand-rule {
    position: absolute; left: 300px; top: 140px; width: 420px; height: 2px;
    background: var(--green-mid);
  }
  .decor-circle {
    position: absolute; right: 40px; top: 100px; width: 150px; height: 150px;
    border-radius: 50%; background: var(--green-pale); opacity: .55;
  }
  .name-block {
    position: absolute; left: 0; top: 160px; width: 260px; height: 120px;
    background: linear-gradient(135deg, var(--green-light), var(--green-mid));
    color: #fff; padding: 34px 0 0 24px;
  }
  .name-block__name { font-weight: 700; font-size: 17px; letter-spacing: .3px; white-space: nowrap; }
  .name-block__role { font-weight: 400; font-size: 16px; margin-top: 4px; }

  .contact-list { position: absolute; left: 284px; top: 178px; list-style: none; }
  .contact-list li {
    display: flex; align-items: center; gap: 10px;
    font-size: 15px; color: var(--text-grey); line-height: 24px;
  }
  .contact-list svg { width: 14px; height: 14px; flex: none; }

  .address-band {
    position: absolute; left: 0; right: 0; bottom: 0; height: 54px;
    background: linear-gradient(90deg, var(--green-mid), var(--green-deep));
    color: #fff; font-size: 15px; letter-spacing: .3px;
    display: flex; align-items: center; justify-content: flex-end; padding-right: 30px;
  }
  .address-band::before {
    content: ""; position: absolute; left: 0; top: -10px; width: 100%; height: 10px;
    background: var(--green-pale); opacity: .6;
  }

  /* back */
  .back-rule { position: absolute; left: 0; right: 0; height: 2px; background: #fff; }
  .back-rule--top { top: 70px; }
  .back-brand {
    position: absolute; left: 60px; top: 84px;
    display: flex; align-items: center; gap: 18px;
  }
  .back-brand__name { font-weight: 300; font-size: 50px; line-height: 1; }
  .back-brand__dot { width: 46px; height: 46px; border-radius: 50%; background: rgba(255,255,255,.55); }
  .appointment {
    position: absolute; left: 60px; right: 60px; top: 180px; height: 112px;
    background: #fff; border-radius: 10px;
    display: flex; flex-direction: column; justify-content: center; gap: 20px;
    padding: 0 24px; color: var(--green-ink); font-size: 14px;
  }
  .appointment__row { display: flex; align-items: flex-end; gap: 8px; }
  .appointment__label { white-space: nowrap; }
  .appointment__line { flex: 1; border-bottom: 1px solid var(--green-ink); height: 1px; margin-bottom: 4px; }
  .appointment__line--short { flex: .6; }
  .notice {
    position: absolute; left: 0; right: 0; bottom: 44px; text-align: center;
    font-size: 16px; letter-spacing: .2px;
  }
</style>
</head>
<body>
<main class="canvas">

  <section class="card card--front" aria-label="Business card front">
    <div class="corner-square"></div>
    <div class="decor-circle"></div>
    <div class="brand">
      <span class="brand__dot"></span>
      <span class="brand__name">Brightwell<br>Dental Care</span>
    </div>
    <div class="brand-rule"></div>

    <div class="name-block">
      <div class="name-block__name">MARLOW T. BENNING DDS</div>
      <div class="name-block__role">Dentist</div>
    </div>

    <ul class="contact-list">
      <li>
        <svg viewBox="0 0 14 14"><rect width="14" height="14" rx="2" fill="#5cb338"/><rect x="4.5" y="2.5" width="5" height="9" rx="1" fill="none" stroke="#fff" stroke-width="1.2"/></svg>
        (248)555-0193
      </li>
      <li>
        <svg viewBox="0 0 14 14"><rect width="14" height="14" rx="2" fill="#5cb338"/><rect x="3" y="5" width="8" height="6" fill="none" stroke="#fff" stroke-width="1.2"/><rect x="4.5" y="2.5" width="5" height="2.5" fill="#fff"/></svg>
        (248)555-0147
      </li>
      <li>
        <svg viewBox="0 0 14 14"><rect width="14" height="14" rx="2" fill="#5cb338"/><rect x="2.5" y="4" width="9" height="6" fill="none" stroke="#fff" stroke-width="1.2"/><path d="M2.5 4 7 7.5 11.5 4" fill="none" stroke="#fff" stroke-width="1.2"/></svg>
        info@BrightwellDentalCareMi.example
      </li>
      <li>
        <svg viewBox="0 0 14 14"><rect width="14" height="14" rx="2" fill="#5cb338"/><circle cx="7" cy="7" r="4" fill="none" stroke="#fff" stroke-width="1.2"/><path d="M3 7h8M7 3v8" stroke="#fff" stroke-width="1"/></svg>
        www.BrightwellDentalCareMi.example
      </li>
    </ul>

    <div class="address-band">2740 W. Hollister Rd. Ste. 7 Royal Oak, MI 48133</div>
  </section>

  <section class="card card--back" aria-label="Business card back, appointment reminder">
    <div class="back-rule back-rule--top"></div>
    <div class="back-brand">
      <span class="back-brand__name">Brightwell Dental Care</span>
      <span class="back-brand__dot"></span>
    </div>
    <div class="appointment">
      <div class="appointment__row">
        <span class="appointment__label">For:</span>
        <span class="appointment__line"></span>
      </div>
      <div class="appointment__row">
        <span class="appointment__label">Date:</span>
        <span class="appointment__line"></span>
        <span class="appointment__label">Time:</span>
        <span class="appointment__line appointment__line--short"></span>
      </div>
    </div>
    <p class="notice">If you are unable to keep your appointment, kindly give 48 hours notice</p>
  </section>

</main>
</body>
</html>
```